Rocket business card

Modern business card design, use of color is good with clean space too.

Things to include on card:

Quote: I add fuel to your optometry practice

- Eyewear Sales
- Admin Duties
- Revenue Collection
- Leadership
- Tech Adoption
- COGS Reduction
- Product Sourcing
-Medical Growth

Dalton Vessey, CEO
Glint Harbor
Text Me! 847-302-1964
dalton@glintharbor.example

```html
<!DOCTYPE html>
<html lang="en">
<head>
<meta charset="utf-8">
<title>Glint Harbor — Business Card</title>
<link rel="stylesheet" href="https://fonts.googleapis.com/css2?family=Josefin+Sans:wght@300;600&family=Open+Sans:wght@400&family=Arimo:wght@400&display=swap">
<style>
  :root {
    --page: #ffffff;
    --ink-black: #000000;
    --ink-dark: #1e1714;
    --orange: #f18a2a;
    --orange-light: #f6a623;
    --list-orange: #f4a21f;
    --white: #ffffff;
    --tagline: #b9b9b9;
    --contact: #111111;
  }
  * { margin: 0; padding: 0; box-sizing: border-box; }
  html, body {
    width: 960px; height: 1200px; overflow: hidden;
    background: var(--page);
  }
  .canvas { position: relative; width: 960px; height: 1200px; }
  .card {
    position: absolute; left: 61px; width: 839px; height: 480px; overflow: hidden;
  }
  .card-front { top: 78px; background: var(--ink-black); }
  .card-back { top: 640px; height: 478px; }

  .brand-dot {
    position: absolute; left: 351px; top: 132px; width: 136px; height: 136px;
    border-radius: 50%; background: var(--orange);
  }
  .brand-name {
    position: absolute; left: 0; right: 0; top: 290px; text-align: center;
    font-family: "Josefin Sans", sans-serif; font-weight: 600; font-size: 60px;
    letter-spacing: 2px; color: var(--white); line-height: 1;
  }
  .tagline {
    position: absolute; left: 0; right: 0; top: 356px; text-align: center;
    font-family: "Josefin Sans", sans-serif; font-weight: 300; font-size: 19px;
    letter-spacing: 1px; color: var(--tagline);
  }

  .back-shapes { position: absolute; inset: 0; }
  .services {
    position: absolute; left: 43px; top: 70px; list-style: none;
    font-family: "Open Sans", sans-serif; font-size: 29px; line-height: 43.2px;
    color: var(--list-orange); letter-spacing: 0.5px;
  }
  .services li::before { content: "- "; }
  .contact {
    position: absolute; right: 36px; top: 178px; text-align: right;
    font-family: "Arimo", sans-serif; color: var(--contact); letter-spacing: 1px;
  }
  .contact-name { font-size: 29px; line-height: 38px; }
  .contact-company { font-size: 21px; line-height: 30px; }
  .contact-phone { font-size: 21px; line-height: 30px; letter-spacing: 1.5px; }
  .contact-email { font-size: 21px; line-height: 30px; letter-spacing: 0.3px; }
</style>
</head>
<body>
<div class="canvas">
  <section class="card card-front">
    <div class="brand-dot"></div>
    <div class="brand-name">GLINT HARBOR</div>
    <p class="tagline">I add fuel to your optometry practice</p>
  </section>

  <section class="card card-back">
    <svg class="back-shapes" width="839" height="478" viewBox="0 0 839 478">
      <defs>
        <linearGradient id="orangeFill" x1="0" y1="0" x2="1" y2="0">
          <stop offset="0" stop-color="#ec8528"/>
          <stop offset="1" stop-color="#f6a623"/>
        </linearGradient>
      </defs>
      <rect class="orange-field" width="839" height="478" fill="url(#orangeFill)"/>
      <path class="outer-band" d="M0 0 H402 Q570 239 403 478 H0 Z" fill="#1e1714"/>
      <path class="accent-stripe" d="M0 0 H366 Q540 239 363 478 H0 Z" fill="#ee8a26"/>
      <path class="inner-panel" d="M0 0 H351 Q533 239 349 478 H0 Z" fill="#1e1714"/>
    </svg>
    <ul class="services">
      <li>Eyewear Sales</li>
      <li>Admin Duties</li>
      <li>Revenue Collection</li>
      <li>Leadership</li>
      <li>Tech Adoption</li>
      <li>COGS Reduction</li>
      <li>Product Sourcing</li>
      <li>Medical Growth</li>
    </ul>
    <div class="contact">
      <p class="contact-name">Dalton Vessey, CEO</p>
      <p class="contact-company">Glint Harbor</p>
      <p class="contact-phone">Text Me! 847-302-1964</p>
      <p class="contact-email">dalton@glintharbor.example</p>
    </div>
  </section>
</div>
</body>
</html>
```